Catchy Cards for Hospital

I run a rural hospital in Verdan called Pellor Valley Hospital and am in need of contemporary business cards for all of my Department Heads. While our logo is somewhat simplistic, I don't have the option of changing it at this time, so anything to make the rest of the card present the appearance of a modern, professional healthcare facility would be great. Although the attached files are in black, our hospital colors are in a copper brown and black. I need to be able to change the name and title on the card so I can get cards printed for various department heads.

Target Market(s)

Referring physicians, large hospital systems, national organizations, state and federal government

Industry/Entity Type

Hospital

Contact Information for Business Card

Name Dale Hoskin
Title CEO

Phone: Main 325-555-0147 & Direct xxxxxx
Fax xxxxx
dale.hoskin@pellorvh.example
382 Wimble Street Box 415
Harlow, Verdan 76902

Font styles to use
Serif

Colors
f48340

Requirements
Must have
• Clean crisp lines and ability to modify names, titles and emails
• On the back "PellorValleyHospital.Example
Nice to have
• Needs to be in line with logo, which is a bit dated and not too appealing, but I'm hoping that the rest of the card can make up for that fact just a little bit.
• Hospital's colors are a copper brown, black and white
Should not have
• Shapes or anything distracting

```html
<!DOCTYPE html>
<html lang="en">
<head>
<meta charset="utf-8">
<title>Pellor Valley Hospital – Business Card</title>
<link rel="stylesheet" href="https://fonts.googleapis.com/css2?family=Open+Sans:wght@400;600;700&display=swap">
<style>
  :root {
    --backdrop: #111111;
    --copper: #561c10;
    --name-red: #6e1a0f;
    --ink: #050505;
    --paper: #f7f5f0;
    --white: #ffffff;
  }
  * { box-sizing: border-box; margin: 0; padding: 0; }
  html, body { width: 1200px; height: 1000px; overflow: hidden; }
  body {
    background: var(--backdrop);
    font-family: "Open Sans", Arial, sans-serif;
    position: relative;
  }
  .card {
    position: absolute;
    width: 500px;
    height: 286px;
    overflow: hidden;
  }

  /* Back of card */
  .card-back {
    left: 70px;
    top: 200px;
    background: var(--copper);
  }
  .back-seal {
    position: absolute;
    left: 250px;
    top: 62px;
    width: 124px;
    height: 108px;
    border-radius: 50%;
    background: var(--paper);
    display: flex;
    align-items: center;
    justify-content: center;
  }
  .wordmark {
    color: var(--ink);
    font-weight: 700;
    line-height: 1.05;
    text-align: left;
  }
  .back-seal .wordmark { font-size: 15px; }
  .back-url {
    position: absolute;
    left: 44px;
    bottom: 54px;
    color: var(--paper);
    font-size: 15px;
    letter-spacing: 0.1px;
  }

  /* Front of card */
  .card-front {
    left: 630px;
    top: 500px;
    background: var(--paper);
  }
  .front-bands {
    position: absolute;
    inset: 0;
  }
  .holder {
    position: absolute;
    left: 44px;
    top: 38px;
  }
  .holder-name {
    color: var(--name-red);
    font-weight: 700;
    font-size: 19px;
    line-height: 1.1;
  }
  .holder-title {
    color: var(--ink);
    font-size: 16px;
    line-height: 1.2;
  }
  .front-mark {
    position: absolute;
    right: 34px;
    top: 44px;
  }
  .front-mark .wordmark { font-size: 24px; }
  .contact-list {
    position: absolute;
    left: 36px;
    top: 120px;
    list-style: none;
    color: var(--white);
    font-size: 12px;
    line-height: 17px;
  }
  .contact-list li {
    display: flex;
    align-items: center;
    gap: 9px;
  }
  .contact-list svg { width: 11px; height: 11px; flex: none; }
  .address {
    position: absolute;
    right: 36px;
    top: 176px;
    color: var(--paper);
    font-size: 13px;
    line-height: 19px;
    text-align: right;
  }
</style>
</head>
<body>

  <section class="card card-back" aria-label="Business card back">
    <div class="back-seal">
      <div class="wordmark">Pellor<br>Valley<br>Hospital</div>
    </div>
    <p class="back-url">PellorValleyHospital.Example</p>
  </section>

  <section class="card card-front" aria-label="Business card front">
    <svg class="front-bands" viewBox="0 0 500 286" aria-hidden="true">
      <polygon points="20,110 340,110 270,200 20,200" fill="var(--ink)"/>
      <polygon points="309,150 480,150 480,246 235,246" fill="var(--copper)"/>
    </svg>

    <div class="holder">
      <p class="holder-name">Dale Hoskin</p>
      <p class="holder-title">CEO</p>
    </div>

    <div class="front-mark">
      <div class="wordmark">Pellor<br>Valley<br>Hospital</div>
    </div>

    <ul class="contact-list">
      <li>
        <svg viewBox="0 0 12 12"><path d="M3 1l2 2.5-1.2 1.2a7 7 0 0 0 3.5 3.5L8.5 7 11 9l-1 2C5 11 1 7 1 2z" fill="currentColor"/></svg>
        Main 325 555 0147
      </li>
      <li>
        <svg viewBox="0 0 12 12"><circle cx="6" cy="3.5" r="2.5" fill="currentColor"/><path d="M1 11c0-3 2.2-5 5-5s5 2 5 5z" fill="currentColor"/></svg>
        Direct 325 555 0182
      </li>
      <li>
        <svg viewBox="0 0 12 12"><rect x="3" y="1" width="6" height="3" fill="none" stroke="currentColor"/><rect x="1" y="4" width="10" height="5" fill="currentColor"/><rect x="3" y="8" width="6" height="3" fill="none" stroke="currentColor"/></svg>
        325 555 0193
      </li>
      <li>
        <svg viewBox="0 0 12 12"><rect x="1" y="2.5" width="10" height="7" fill="currentColor"/><path d="M1 2.5l5 4 5-4" fill="none" stroke="#000" stroke-width="1"/></svg>
        dale.hoskin@pellorvh.example
      </li>
    </ul>

    <p class="address">382 Wimble Street<br>Box 415 Harlow<br>Verdan 76902</p>
  </section>

</body>
</html>
```